Quartz Owl needs Bad-Ass Design!
Professional
Thos. Carl Pemberton
Owner
P.O. Box 27815 Coral Bend, KS. 96218
carlpemberton@k9ventura.us.com
http://www.k9ventura.us.com

```html
<!DOCTYPE html>
<html lang="en">
<head>
<meta charset="utf-8">
<title>Quartz Owl — Business Card</title>
<link rel="stylesheet" href="https://fonts.googleapis.com/css2?family=Arimo:wght@400;700&display=swap">
<style>
  :root {
    --backdrop: #e9e9ec;
    --card: #f4f4f6;
    --card-shade: #dcdde2;
    --brand-blue: #1f4f9e;
    --brand-red: #e0262b;
    --ink: #2b2b30;
    --ink-soft: #55565c;
    --rule: #1f4f9e;
  }
  * { margin: 0; padding: 0; box-sizing: border-box; }
  html, body { width: 1200px; height: 737px; overflow: hidden; }
  body {
    background: var(--backdrop);
    font-family: "Arimo", Arial, sans-serif;
    color: var(--ink);
    position: relative;
  }
  .business-card {
    position: absolute;
    left: 160px; top: 108px;
    width: 880px; height: 520px;
    border-radius: 14px;
    overflow: hidden;
    background: radial-gradient(ellipse at 55% 50%, #ffffff 0%, var(--card) 55%, var(--card-shade) 100%);
    box-shadow: 0 10px 30px rgba(0,0,0,0.18);
  }
  .card-swooshes { position: absolute; inset: 0; width: 100%; height: 100%; }
  .brand-lockup {
    position: absolute;
    left: 455px; top: 118px;
  }
  .brand-row { display: flex; align-items: center; gap: 14px; }
  .brand-mark {
    width: 30px; height: 30px;
    background: var(--brand-blue);
  }
  .brand-name {
    font-size: 44px; font-weight: 700;
    color: var(--brand-blue);
    letter-spacing: -0.5px;
    line-height: 1;
  }
  .brand-tagline {
    margin-left: 46px; margin-top: 6px;
    font-size: 13px; color: var(--ink-soft);
  }
  .holder {
    position: absolute;
    right: 484px; top: 330px;
    text-align: right;
  }
  .holder-name {
    font-size: 22px; font-weight: 700;
    text-transform: uppercase;
    letter-spacing: 0.3px;
  }
  .holder-title {
    margin-top: 8px; margin-right: 60px;
    font-size: 15px; color: var(--ink-soft);
  }
  .holder-rule {
    position: absolute;
    left: 0; top: 402px;
    width: 420px; height: 2px;
    background: var(--rule);
  }
  .holder-email {
    position: absolute;
    left: 22px; top: 418px;
    font-size: 15px; color: var(--ink-soft);
  }
  .contact-block {
    position: absolute;
    left: 448px; top: 246px;
    font-size: 15px; line-height: 29px;
    color: var(--ink-soft);
    list-style: none;
  }
  .contact-label { color: var(--brand-blue); font-weight: 700; }
</style>
</head>
<body>
  <article class="business-card">
    <svg class="card-swooshes" viewBox="0 0 880 520" preserveAspectRatio="none" aria-hidden="true">
      <path d="M0 0 H880 V18 C620 22 300 40 0 100 Z" fill="var(--brand-blue)"/>
      <path d="M0 100 C300 40 620 22 880 18 V26 C620 32 300 54 0 116 Z" fill="var(--brand-red)"/>
      <path d="M0 468 C320 470 620 440 880 388 V402 C620 452 320 482 0 482 Z" fill="var(--brand-red)"/>
      <path d="M0 482 C320 482 620 452 880 402 V520 H0 Z" fill="var(--brand-blue)"/>
    </svg>

    <div class="brand-lockup">
      <div class="brand-row">
        <span class="brand-mark"></span>
        <span class="brand-name">Quartz Owl</span>
      </div>
      <p class="brand-tagline">Tech help around the clock</p>
    </div>

    <div class="holder">
      <h1 class="holder-name">Thos. Carl Pemberton</h1>
      <p class="holder-title">Owner</p>
    </div>
    <div class="holder-rule"></div>
    <p class="holder-email">carlpemberton@k9ventura.us.com</p>

    <ul class="contact-block">
      <li>P.O. Box 27815</li>
      <li>Coral Bend, KS. 96218</li>
      <li><span class="contact-label">Phone :</span> (808) 555-0147</li>
      <li><span class="contact-label">Web :</span> www.k9ventura.us.com</li>
    </ul>
  </article>
</body>
</html>
```